Akademie für Gestaltung Lindenhof sucht Plakat-Design für Veranstaltung
Zielgruppe
Wird sind die Akademie für Gestaltung Lindenhof. Es handelt sich um die Veranstaltung 'Werkschau Abend'. Die Zielgruppe sind Personen, die sich für neue Technologien interessieren. Studenten präsentieren ihre Projekte die sie übers Semester erarbeitet haben.
Die Werkschau Abend findet am 31.01.2019 statt. Alle Informationen müssen ersichtlich auf dem Plakat sein
Akademie für Gestaltung Lindenhof
Kastanienweg. 7
70412 Stuttgart
Aufgabenstellung
Es soll schlich gehalten werden.

```html
<!DOCTYPE html>
<html lang="de">
<head>
<meta charset="utf-8">
<title>Werkschau Abend – Plakat</title>
<link rel="stylesheet" href="https://fonts.googleapis.com/css2?family=Orbitron:wght@400;500&family=Source+Sans+3:wght@400&display=swap">
<style>
  :root {
    --stage: #2a2a2c;
    --paper: #ededee;
    --photo-light: #f2f2f3;
    --photo-mid: #d9d9db;
    --ink: #111111;
    --accent: #e0003c;
    --date-grey: #9a9a9a;
    --credit: #333333;
  }
  html, body {
    margin: 0;
    padding: 0;
    width: 1200px;
    height: 2786px;
    overflow: hidden;
    background: var(--stage);
  }
  .poster {
    position: absolute;
    left: 0;
    top: 544px;
    width: 1200px;
    height: 1697px;
    background: var(--paper);
    overflow: hidden;
  }
  .poster__photo {
    position: absolute;
    left: 0;
    top: 0;
    width: 1200px;
    height: 1697px;
    display: block;
  }
  .poster__credit {
    position: absolute;
    left: 30px;
    top: 360px;
    transform: rotate(-90deg);
    transform-origin: left top;
    font-family: "Source Sans 3", sans-serif;
    font-size: 11px;
    color: var(--credit);
    white-space: nowrap;
  }
  .poster__title {
    position: absolute;
    left: 540px;
    top: 1580px;
    transform: rotate(-90deg);
    transform-origin: left top;
    margin: 0;
    font-family: "Orbitron", sans-serif;
    font-weight: 400;
    font-size: 62px;
    line-height: 1;
    white-space: nowrap;
  }
  .poster__title-first { color: var(--accent); }
  .poster__title-second { color: var(--ink); margin-left: 22px; }
  .poster__date { color: var(--date-grey); margin-left: 48px; }
  .poster__mark {
    position: absolute;
    left: 84px;
    top: 1524px;
    width: 30px;
    height: 30px;
    background: var(--accent);
  }
  .poster__address {
    position: absolute;
    left: 720px;
    top: 1488px;
    margin: 0;
    font-family: "Source Sans 3", sans-serif;
    font-style: normal;
    font-size: 28px;
    line-height: 1.5;
    color: var(--ink);
  }
</style>
</head>
<body>
  <main class="poster">
    <svg class="poster__photo" viewBox="0 0 1200 1697" role="img" aria-label="Foto: Ausschnitt einer silbernen Laptop-Tastatur mit Pfeiltasten und abgerundeter Gehäuseecke auf hellem Grund">
      <defs>
        <linearGradient id="laptop-tone" x1="0" y1="0" x2="1" y2="1">
          <stop offset="0" stop-color="#cfcfd1"/>
          <stop offset="1" stop-color="#e6e6e8"/>
        </linearGradient>
      </defs>
      <rect width="1200" height="1697" fill="var(--photo-light)"/>
      <path d="M0 0 H820 V1100 Q820 1205 715 1205 H0 Z" fill="url(#laptop-tone)"/>
      <rect x="0" y="0" width="690" height="260" fill="var(--photo-mid)"/>
    </svg>
    <div class="poster__credit">Photo by Jonas Feldmann on Bildarchiv Nord</div>
    <h1 class="poster__title"><span class="poster__title-first">Werkschau</span><span class="poster__title-second">Abend</span><span class="poster__date">31.01.2019</span></h1>
    <div class="poster__mark"></div>
    <address class="poster__address">Akademie für Gestaltung Lindenhof<br>Kastanienweg 7<br>70412 Stuttgart</address>
  </main>
</body>
</html>
```